Songs Cover Art. Song tittle DJ K - Turn the Lights Low

Hey

I need a cover art for my songs. My genre is Big Room House/EDM music and my DJ name is DJ K. Song title is Turn the Lights Low. I'm a producer and i need a designer to design all my cover art so that i will be able upload my song with a cover art. Do let me know if you have any questions.

Song Tittle: Turn the Lights Low
Artist name: DJ K

Thanks

Reason: I will give more time in order for you guys to create more design!

Industry/Entity Type

House

Requirements
Should not have
• Please dont make the design to colourful.

```html
<!DOCTYPE html>
<html lang="en">
<head>
<meta charset="utf-8">
<title>DJ K – Turn the Lights Low</title>
<link rel="stylesheet" href="https://fonts.googleapis.com/css2?family=Teko:wght@400;600&display=swap">
<style>
  :root {
    --glow-white: #fff8e6;
    --glow-yellow: #ffd54a;
    --amber: #f29a1c;
    --orange: #d9630f;
    --rust: #9c2f0c;
    --ember: #5a1406;
    --crowd-dark: #120403;
    --title-ink: #0b0605;
    --title-echo: rgba(226, 70, 20, 0.75);
    --artist-ink: #ffffff;
  }
  html, body {
    margin: 0;
    padding: 0;
    width: 1200px;
    height: 1200px;
    overflow: hidden;
    background: var(--crowd-dark);
  }
  .cover {
    position: relative;
    width: 1200px;
    height: 1200px;
    overflow: hidden;
  }
  .cover__backdrop {
    position: absolute;
    inset: 0;
    background:
      radial-gradient(circle at 50% 44%, var(--glow-white) 0%, var(--glow-yellow) 16%, var(--amber) 36%, var(--orange) 58%, var(--rust) 82%, var(--ember) 100%);
  }
  .cover__crowd {
    position: absolute;
    left: 0;
    right: 0;
    bottom: 0;
    height: 520px;
    background:
      radial-gradient(ellipse at 50% 20%, rgba(230, 40, 60, 0.55) 0%, rgba(120, 20, 10, 0.35) 30%, rgba(0, 0, 0, 0) 60%),
      linear-gradient(to bottom, rgba(18, 4, 3, 0) 0%, rgba(60, 14, 6, 0.7) 28%, var(--crowd-dark) 60%, var(--crowd-dark) 100%);
  }
  .artist {
    position: absolute;
    top: 52px;
    left: 0;
    width: 100%;
    margin: 0;
    text-align: center;
    font-family: "Teko", sans-serif;
    font-weight: 400;
    font-size: 84px;
    line-height: 1;
    letter-spacing: 3px;
    color: var(--artist-ink);
  }
  .title {
    position: absolute;
    top: 398px;
    left: 0;
    width: 100%;
    margin: 0;
    text-align: center;
    font-family: "Teko", sans-serif;
    font-weight: 600;
    font-size: 196px;
    line-height: 148px;
    letter-spacing: 4px;
    text-transform: uppercase;
    color: var(--title-ink);
    text-shadow: 8px 10px 0 var(--title-echo);
  }
  .title__line {
    display: block;
  }
</style>
</head>
<body>
  <main class="cover">
    <div class="cover__backdrop" role="img" aria-label="Blazing orange and gold club light burst with textured festival graphics"></div>
    <div class="cover__crowd" role="img" aria-label="Silhouetted dance crowd with hands raised toward the stage lights"></div>
    <p class="artist">DJ K</p>
    <h1 class="title">
      <span class="title__line">Turn the</span>
      <span class="title__line">Lights Low</span>
    </h1>
  </main>
</body>
</html>
```